Rollin’ Kites Copper Tide beer can design

We are not looking for a new logo, we want to use our current logo!! Current Logo is Attached. We want to incorporate our current logo into a full can design for our new non-alcoholic, THC infused Beer design. We cannot use animals or cartoons. We also can not say beer. We would like to use our main label found at www.rollinkites-example.com
Several ideas include having small images of beer cans and beer mugs all over the can as a background. Another idea is to make it freedom and liberty themed. We want to make sure people understand it is a beer, even though we can say beer on the can.

Target Market(s)

30-50 year olds

Industry/Entity Type

THC beverage

Logo Text

Rollin’ Kites Copper Tide

Colors
59FF00
82FF00
B8FF75
E3FFCB
F4FFEA

Requirements
Must have
• Full 12 oz beer can design
Should not have
• No word beer, do not need a new logo, need a can design

```html
<!DOCTYPE html>
<html lang="en">
<head>
<meta charset="utf-8">
<title>Rollin’ Kites Copper Tide – Can Label</title>
<link rel="stylesheet" href="https://fonts.googleapis.com/css2?family=Oswald:wght@700&family=Montserrat:wght@800&family=Fredoka:wght@700&display=swap">
<style>
  :root {
    --foam: #fbf7e4;
    --foam-shade: #f1e9c6;
    --amber: #f3b51c;
    --amber-light: #fbd24a;
    --amber-deep: #e59e10;
    --ink-green: #1d6b2b;
    --digit-fill: #f7c531;
    --digit-outline: #5a3612;
    --badge-green: #1e6a32;
    --badge-ring: #7cc447;
    --page: #ffffff;
  }
  * { margin: 0; padding: 0; box-sizing: border-box; }
  html, body { width: 800px; height: 1200px; overflow: hidden; background: var(--page); }
  .can-label {
    position: relative;
    width: 800px;
    height: 1200px;
    overflow: hidden;
  }
  .liquid-background {
    position: absolute;
    inset: 0;
    background:
      radial-gradient(ellipse at 30% 45%, var(--amber-light) 0%, transparent 60%),
      linear-gradient(180deg, var(--amber-deep) 0%, var(--amber) 40%, var(--amber-deep) 100%);
  }
  .foam-head {
    position: absolute;
    left: 0; top: 0;
    width: 800px; height: 230px;
  }
  .brand-title {
    position: absolute;
    top: 258px;
    width: 100%;
    text-align: center;
    font-family: "Oswald", sans-serif;
    font-weight: 700;
    font-size: 104px;
    line-height: 1;
    color: var(--ink-green);
    letter-spacing: 1px;
  }
  .brand-subtitle {
    position: absolute;
    top: 380px;
    width: 100%;
    text-align: center;
    font-family: "Montserrat", sans-serif;
    font-weight: 800;
    font-size: 52px;
    line-height: 1;
    color: var(--ink-green);
    letter-spacing: 3px;
  }
  .strength-figure {
    position: absolute;
    top: 430px;
    left: 50px;
    font-family: "Fredoka", sans-serif;
    font-weight: 700;
    font-size: 470px;
    line-height: 1;
    color: var(--digit-fill);
    -webkit-text-stroke: 14px var(--digit-outline);
    paint-order: stroke fill;
    letter-spacing: -10px;
  }
  .infusion-note {
    position: absolute;
    top: 895px;
    right: 70px;
    text-align: center;
    font-family: "Oswald", sans-serif;
    font-weight: 700;
    color: var(--ink-green);
    line-height: 1;
  }
  .infusion-note .thc { display: block; font-size: 70px; }
  .infusion-note .infused { display: block; font-size: 36px; margin-top: 4px; }
  .brand-mark {
    position: absolute;
    top: 1010px;
    left: 0;
    width: 100%;
    display: flex;
    align-items: center;
    justify-content: center;
    gap: 22px;
  }
  .brand-mark .dot {
    width: 70px; height: 70px;
    border-radius: 50%;
    background: var(--badge-green);
  }
  .brand-mark .name {
    font-family: "Oswald", sans-serif;
    font-weight: 700;
    font-size: 58px;
    color: var(--badge-green);
  }
  .site-address {
    position: absolute;
    bottom: 48px;
    width: 100%;
    text-align: center;
    font-family: "Montserrat", sans-serif;
    font-weight: 800;
    font-size: 22px;
    color: var(--ink-green);
    letter-spacing: 1px;
  }
</style>
</head>
<body>
  <main class="can-label">
    <div class="liquid-background" role="img" aria-label="Golden amber liquid background scattered with rising bubbles"></div>

    <svg class="foam-head" viewBox="0 0 800 230" aria-hidden="true">
      <path d="M0 0 H800 V200 C760 190 740 215 700 205 C650 192 620 210 570 200 C520 190 480 212 430 204 C380 196 340 214 290 204 C240 194 200 212 150 203 C100 194 60 214 0 202 Z" fill="var(--foam)"/>
      <path d="M0 175 C80 190 160 170 240 182 C330 196 420 172 520 184 C610 195 700 176 800 184 V200 C760 190 740 215 700 205 C650 192 620 210 570 200 C520 190 480 212 430 204 C380 196 340 214 290 204 C240 194 200 212 150 203 C100 194 60 214 0 202 Z" fill="var(--foam-shade)"/>
    </svg>

    <h1 class="brand-title">ROLLIN’ KITES</h1>
    <p class="brand-subtitle">COPPER TIDE</p>

    <div class="strength-figure">0%</div>

    <p class="infusion-note"><span class="thc">THC</span><span class="infused">INFUSED</span></p>

    <div class="brand-mark">
      <span class="dot"></span>
      <span class="name">Rollin’ Kites</span>
    </div>

    <p class="site-address">www.rollinkites-example.com</p>
  </main>
</body>
</html>
```